Business card design for Kovantrix

I need a business card based on the logo design produced for Kovantrix. The company is focused on triathlon and endurance sport coaching and the tag line is (per the logo) "Stamina. Discipline. Performance". The design should be sophisticated, appropriate to an affluent and business oriented target market. Colors are optional but the color of the logo probably dictates the color used on the card. I envisage using the red logo, with black print for the wording and contact numbers on a white or cream background, but am open to alternative suggestions. I expect to select something fairly conventional, but would like to see some designs that are less conventional to stretch my thinking on what could be appropriate. I am assuming a single side design is best, but willing to consider double sided as an option.

Target Market(s)

Individual athletes and corporate health and wellness leaders

Industry/Entity Type

Health And Wellness

Contact Information for Business Card

The card should provide the following information:
Logo
My name: Marcus Bellingham
Company website: Kovantrix.com
My email: marcus.bellingham@kovantrix.com
My cell phone number: +1-555-812-6093

Font styles to use
Sans Serif

Colors

Designer to choose colors to be used in the design.

Requirements
Must have
• Space on the card - simple design, not over crowded.
Nice to have
• clean and clear font, nothing garish or mass market like
Should not have
• Do not add pictures

```html
<!DOCTYPE html>
<html lang="en">
<head>
<meta charset="utf-8">
<title>Kovantrix Business Card</title>
<link rel="stylesheet" href="https://fonts.googleapis.com/css2?family=Open+Sans:wght@400;600;700&display=swap">
<style>
  :root {
    --brand-red: #b0262a;
    --ink: #1e1e1e;
    --card-white: #fbfbfb;
    --backdrop: #e6e4e2;
  }
  * { margin: 0; padding: 0; box-sizing: border-box; }
  html, body {
    width: 1200px;
    height: 900px;
    overflow: hidden;
    background: var(--backdrop);
    font-family: "Open Sans", sans-serif;
  }
  .business-card {
    position: absolute;
    left: 150px;
    top: 180px;
    width: 900px;
    height: 540px;
    background: var(--card-white);
    border-radius: 22px;
    overflow: hidden;
    box-shadow: 0 10px 30px rgba(0,0,0,0.12);
    text-align: center;
  }
  .wordmark {
    position: absolute;
    top: 112px;
    left: 0;
    width: 100%;
    font-size: 86px;
    font-weight: 600;
    line-height: 1;
    color: var(--brand-red);
    letter-spacing: -1px;
  }
  .tagline {
    position: absolute;
    top: 200px;
    left: 0;
    width: 100%;
    font-size: 28px;
    font-weight: 400;
    line-height: 1;
    color: var(--ink);
    letter-spacing: 0.5px;
  }
  .contact-name {
    position: absolute;
    top: 282px;
    left: 0;
    width: 100%;
    font-size: 34px;
    font-weight: 600;
    line-height: 1;
    color: var(--brand-red);
  }
  .contact-list {
    position: absolute;
    top: 334px;
    left: 0;
    width: 100%;
    list-style: none;
    font-size: 26px;
    line-height: 33px;
    color: var(--ink);
  }
  .contact-label {
    color: var(--brand-red);
    font-weight: 600;
  }
  .stripe-dark {
    position: absolute;
    left: 0;
    top: 453px;
    width: 100%;
    height: 26px;
    background: var(--ink);
  }
  .stripe-red {
    position: absolute;
    left: 0;
    top: 479px;
    width: 100%;
    height: 61px;
    background: var(--brand-red);
  }
</style>
</head>
<body>
  <div class="business-card">
    <div class="wordmark">Kovantrix</div>
    <div class="tagline">STAMINA. DISCIPLINE. PERFORMANCE</div>
    <div class="contact-name">Marcus Bellingham</div>
    <ul class="contact-list">
      <li><span class="contact-label">M</span>: +1-555-812-6093</li>
      <li><span class="contact-label">E</span>: marcus.bellingham@kovantrix.com</li>
      <li><span class="contact-label">W</span>: www.Kovantrix.com</li>
    </ul>
    <div class="stripe-dark"></div>
    <div class="stripe-red"></div>
  </div>
</body>
</html>
```